An anniversary gift for my girlfriend

My girlfriend and I have been dating for almost 2 years. We met online and this has afforded us the really unique opportunity to have the first words we said to each other (the whole conversation, in fact) preserved. We're moving in together in a few months and she doesn't know that I saved the conversation. I've been waiting for this to turn it into something we can hang in our new place.

The only phrase I want to use is:
"Well if you dislike people's knees then I think we'll get along famously"

It's an Nobody Leaves Before Midnight in Portland reference for the curious.

I want the poster to use the words themselves as the art; I'm thinking typography. I'd like it to match her aesthetic, she likes to wear Nora Vell and T. Brisk. Colors shouldn't be anything too "girly". Somewhere I'd like to include the date June 1, 2015. It shouldn't be a major piece of the poster though, just a way to denote the date.

It should fit (and be fully visible in) a 16x20 (inches) frame

Thanks in advance for the work!

Requirements
Must have
• Must use only the words: "Well if you dislike people's knees then I think we'll get along famously"
• I want this to be typography, so making the phrase the center of the poster and the art itself.

```html
<!DOCTYPE html>
<html lang="en">
<head>
<meta charset="utf-8">
<title>Well If You Dislike People's Knees — Typographic Poster</title>
<link rel="stylesheet" href="https://fonts.googleapis.com/css2?family=Playfair+Display:wght@700;900&family=Montserrat:wght@500&display=swap">
<style>
  :root {
    --ink: #141210;
    --ink-soft: rgba(20, 18, 16, 0.14);
    --paper: #faf5ea;
    --wash-apricot: #f2b27f;
    --wash-blush: #fbe2dc;
    --wash-sage: #b8d0c6;
    --wash-butter: #f4eec9;
  }
  html, body {
    margin: 0;
    padding: 0;
    overflow: hidden;
    background: var(--paper);
  }
  .poster {
    position: relative;
    width: 960px;
    height: 1200px;
    overflow: hidden;
    background: var(--paper);
  }
  .poster__wash {
    position: absolute;
    inset: 0;
    background:
      radial-gradient(circle at 560px 690px, var(--wash-sage) 0, rgba(184,208,198,0.85) 330px, rgba(184,208,198,0) 470px),
      radial-gradient(ellipse 520px 620px at 150px 220px, var(--wash-apricot) 0, rgba(242,178,127,0.7) 55%, rgba(242,178,127,0) 100%),
      radial-gradient(ellipse 520px 560px at 880px 120px, var(--wash-blush) 0, rgba(251,226,220,0) 100%),
      radial-gradient(ellipse 460px 420px at 920px 820px, var(--wash-butter) 0, rgba(244,238,201,0) 100%),
      radial-gradient(ellipse 480px 340px at 760px 1150px, var(--wash-butter) 0, rgba(244,238,201,0) 100%),
      var(--paper);
  }
  .poster__swash {
    position: absolute;
    left: 520px;
    top: 490px;
    width: 230px;
    height: 110px;
    border-radius: 50%;
    background: radial-gradient(ellipse at center, var(--ink-soft) 0, rgba(20,18,16,0) 70%);
  }
  .poster__type {
    position: absolute;
    inset: 0;
  }
  .quote {
    fill: var(--ink);
    font-family: "Playfair Display", Georgia, serif;
  }
  .quote--wide { font-weight: 900; }
  .quote--condensed { font-weight: 700; }
  .date {
    fill: var(--ink);
    font-family: "Montserrat", Arial, sans-serif;
    font-weight: 500;
    font-size: 32px;
    letter-spacing: 1px;
  }
</style>
</head>
<body>
  <main class="poster">
    <div class="poster__wash" role="img" aria-label="Soft watercolour wash in apricot, blush, sage and butter tones"></div>
    <div class="poster__swash" role="img" aria-label="Decorative swash flourish linking I, think and we'll"></div>
    <svg class="poster__type" width="960" height="1200" viewBox="0 0 960 1200" role="img" aria-label="Well if you dislike people's knees then I think we'll get along famously. June 1, 2015">
      <text class="quote quote--condensed" x="58" y="294" font-size="240" textLength="412" lengthAdjust="spacingAndGlyphs">WELL</text>
      <text class="quote quote--wide" x="502" y="192" font-size="100" textLength="374" lengthAdjust="spacingAndGlyphs">IF YOU</text>
      <text class="quote quote--wide" x="502" y="294" font-size="122" textLength="374" lengthAdjust="spacingAndGlyphs">DISLIKE</text>
      <text class="quote quote--wide" x="58" y="384" font-size="104" textLength="428" lengthAdjust="spacingAndGlyphs">PEOPLE'S</text>
      <text class="quote quote--wide" x="502" y="384" font-size="104" textLength="372" lengthAdjust="spacingAndGlyphs">KNEES</text>
      <text class="quote quote--condensed" x="58" y="552" font-size="192" textLength="456" lengthAdjust="spacingAndGlyphs">THEN I</text>
      <text class="quote quote--condensed" x="648" y="474" font-size="88" textLength="178" lengthAdjust="spacingAndGlyphs">THINK</text>
      <text class="quote quote--condensed" x="756" y="564" font-size="64" textLength="144" lengthAdjust="spacingAndGlyphs">WE'LL</text>
      <text class="quote quote--condensed" x="70" y="720" font-size="134" textLength="110" lengthAdjust="spacingAndGlyphs">GET</text>
      <text class="quote quote--condensed" x="180" y="840" font-size="366" textLength="684" lengthAdjust="spacingAndGlyphs">ALONG</text>
      <text class="quote quote--wide" x="84" y="960" font-size="108" textLength="782" lengthAdjust="spacingAndGlyphs">FAMOUSLY</text>
      <text class="date" x="480" y="1086" text-anchor="middle" textLength="284" lengthAdjust="spacingAndGlyphs">JUNE 1, 2015</text>
    </svg>
  </main>
</body>
</html>
```